BRAVOLK PROMOTION GROUP Website

Looking for a website design that clearly and powerfully portrays our unique and effective indoor advertising billboards in our network.

Our TeenyPanels, LargoPanels and TitanFlags are strategically placed in high traffic areas of restaurants, pubs, nightclubs, fitness clubs, colleges and universities, and sports arenas.

Bravolk Promotion Group is our new name. Our current site is www.plorvex.ca with our focus now being entirely on our Out-of-Home media. New website address will be www.bravolkpromotion.ca

We need the following sections:

HOME
PRODUCTS (Drop down menu)
-TeenyPanels
-LargoPanels
-TitanFlags
NETWORKS (Drop down menu)
-Resto-Bar
-Sports
-Campus
EFFECTIVENESS
CAMPAIGNS *This page will show numerous ad campaigns and could be a slide show (see www.plorvex.ca/QJPV_campaigns.html )
BECOME A PARTNER
CONTACT

Please include social media functions on the homepage such as chirpnet/visagebook/workloop

We will be supplying content and photos as required.

Our plan is to have you submit the homepage design to start with, and then we can start judging which styles we like the best and can start narrowing our list. As a second round, we would like to ask the "finalists" to submit a second page (another section of the website) and to see how consistent you are in terms of the look and feel you proposed for the homepage.

Attached is our new logo.

We may require you to upload the final website for us.

Websites that are in similar industry are:
www.trelmuk.com
www.quasplen.com

Industry/Entity Type

Advertising

Requirements
Must have
• Our network offers advertising solutions that feature: Guaranteed Readership,100% Gender Specific, Frequency, and Captive Audience. Purchasing advertising space in our network are small to medium business owners and advertising agencies booking on behalf of their clients.

Site must be professional and modern looking.
Nice to have
• Moving banner or slide show of some type.

```html
<!DOCTYPE html>
<html lang="en">
<head>
<meta charset="utf-8">
<title>Bravolk Promotion Group</title>
<link rel="stylesheet" href="https://fonts.googleapis.com/css2?family=Cinzel:wght@400;500&family=Oswald:wght@500&family=PT+Sans:wght@400;700&family=Arimo:wght@400;700&display=swap">
<style>
:root{
  --blue:#2c5f9e;
  --blue-dark:#1f4f8a;
  --band:#3a6596;
  --nav:#6f6f6f;
  --text:#6a6a6a;
  --muted:#8a8a8a;
  --rule:#d8d8d8;
  --page:#fdfbfc;
  --frame:#b7b7b7;
}
*{box-sizing:border-box;margin:0;padding:0}
html,body{width:1121px;height:1200px;overflow:hidden;background:var(--page)}
body{position:relative;font-family:"PT Sans",Arial,sans-serif;color:var(--text)}
.abs{position:absolute}

/* header */
.brand{left:81px;top:20px;width:192px;height:80px;display:flex;align-items:center;gap:8px}
.brand-mark{width:26px;height:26px;background:var(--blue);flex:none}
.brand-name{font-family:"PT Sans",sans-serif;font-weight:700;font-size:17px;line-height:1.1;color:var(--blue)}
.search{left:767px;top:22px;width:255px;height:31px;display:flex}
.search-field{flex:1;background:linear-gradient(#dcdcdc,#ececec);border:1px solid #d2d2d2;font:13px Arimo,sans-serif;color:#7c7c7c;padding:8px 0 0 12px}
.search-btn{width:34px;height:33px;margin-top:-1px;border:1px solid #222;background:#fff;display:flex;align-items:center;justify-content:center}
.nav{left:273px;top:59px;width:748px;height:42px}
.nav-list{position:absolute;left:0;top:0;display:flex;list-style:none;height:42px;align-items:center;padding-left:39px}
.nav-list li{font-family:"Oswald",sans-serif;font-size:14px;color:#111;margin-right:21px;letter-spacing:.2px}
.nav-list li.current{font-family:"PT Sans",sans-serif;font-weight:700;font-size:16px;color:#fff;margin-right:23px}

/* hero */
.slide{left:80px;top:117px;width:563px;height:339px;background:linear-gradient(100deg,#c9ccc6 0%,#b8bfae 40%,#9aa58a 70%,#b4b7b0 100%)}
.slide-title{position:absolute;left:218px;top:20px;font-family:"Cinzel",serif}
.slide-title .l1{font-size:21px;color:#111;letter-spacing:.5px}
.slide-title .l2{font-size:31px;color:var(--blue);line-height:1;letter-spacing:1px}
.slide-bar{position:absolute;left:0;bottom:0;width:100%;height:41px;background:rgba(60,60,60,.75)}
.dots{position:absolute;left:17px;top:17px;display:flex;gap:2px}
.dots span{width:23px;height:8px;background:#9c9c9c}
.dots span.on{background:#fff}
.tile-a{left:652px;top:117px;width:180px;height:340px;background:linear-gradient(#eef0f2,#cfd3d8 60%,#e9ebee)}
.tile-b{left:839px;top:117px;width:181px;height:340px;background:linear-gradient(120deg,#d9cfc2,#6d7589 45%,#c9b8a6)}

/* about */
.about-title{left:84px;top:474px;font-family:"Cinzel",serif;font-size:41px;color:var(--blue);letter-spacing:1px}
.about-lead{left:84px;top:532px;width:553px;font:700 18px/22px Arimo,sans-serif;color:#8f8f8f;text-align:justify}
.about-body{left:84px;top:590px;width:556px;font-size:11.4px;line-height:24px;text-align:justify}
.more{font:700 12.5px Arimo,sans-serif;color:var(--blue-dark);display:flex;align-items:center;gap:4px}

.feature{left:665px;width:320px}
.feature-head{display:flex;align-items:center;gap:13px}
.feature-icon{width:22px;height:22px;border-radius:50%;background:#5d8fc7;display:flex;align-items:center;justify-content:center}
.feature-head h3{font:400 20px "PT Sans",sans-serif;color:var(--blue);text-decoration:underline;text-underline-offset:3px}
.feature p{margin:15px 0 0 36px;font-size:11px;line-height:18px;text-align:justify}

/* lower */
.sec-title{font-family:"Oswald",sans-serif;font-size:28px;color:var(--blue);top:834px;transform:scaleX(.85);transform-origin:left}
.rule{left:80px;width:941px;height:1px;background:var(--rule)}
.thumb{width:157px;height:150px;border:5px solid var(--frame)}
.thumb-party{left:77px;top:911px;background:linear-gradient(135deg,#e48bd0,#6f2e8c 55%,#2c2f8a)}
.thumb-person{left:582px;top:912px;background:linear-gradient(#c9c5b9,#a99a86 60%,#7a8a9a)}
.item h4{font:400 14px Arimo,sans-serif;color:var(--blue-dark)}
.item p{margin-top:20px;font:12px/14px Arimo,sans-serif;color:#777;text-align:justify}

.copyright{left:85px;top:1110px;font:12.5px Arimo,sans-serif;color:#666}
.social{left:920px;top:1098px;display:flex;gap:3px}
.social span{width:32px;height:32px;border-radius:3px;background:linear-gradient(#a8a8a8,#7c7c7c);border:1px solid #6e6e6e}
.band{left:0;top:1161px;width:1121px;height:39px;background:var(--band)}
</style>
</head>
<body>

<header>
  <div class="abs brand">
    <span class="brand-mark"></span>
    <span class="brand-name">Bravolk Promotion Group</span>
  </div>
  <form class="abs search">
    <div class="search-field">Search</div>
    <div class="search-btn">
      <svg width="28" height="28" viewBox="0 0 28 28"><circle cx="16" cy="11" r="8.5" fill="none" stroke="#111" stroke-width="2"/><line x1="10" y1="17" x2="3" y2="25" stroke="#111" stroke-width="3"/></svg>
    </div>
  </form>
  <nav class="abs nav">
    <svg class="abs" width="748" height="42" viewBox="0 0 748 42"><path d="M36 0H748V42H0Z" fill="#6f6f6f"/></svg>
    <ul class="nav-list">
      <li class="current">Home</li><li>PRODUCTS</li><li>NETWORKS</li><li>EFFECTIVENESS</li><li>CAMPAIGNS</li><li>BECOME A PARTNER</li><li>CONTACT US</li>
    </ul>
  </nav>
</header>
<div class="abs" style="left:81px;top:99px;width:192px;height:2px;background:#777"></div>

<section>
  <div class="abs slide" role="img" aria-label="Businessman standing at an office window overlooking trees">
    <div class="slide-title"><div class="l1">Guaranteed Readership</div><div class="l2">to our clients</div></div>
    <div class="slide-bar"><div class="dots"><span class="on"></span><span></span><span></span><span></span><span></span></div></div>
  </div>
  <div class="abs tile-a" role="img" aria-label="Businessman on the phone in a bright glass atrium"></div>
  <div class="abs tile-b" role="img" aria-label="Business people shaking hands across a desk"></div>
</section>

<section>
  <h2 class="abs about-title">About Us</h2>
  <p class="abs about-lead">Nulla facilisi. Suspendisse non nisi vel neque laoreet tempus eget iaculis sapien.</p>
  <p class="abs about-body">Morbi lacus velit, adipiscing non fringilla sed, accumsan et elit. Nam auctor gravida diam ut sagittis. Duis quis mauris odio. Sed ante urna, aliquet faucibus commodo in, venenatis a justo. Morbi dignissim tristique leo, a auctor arcu rhoncus eget. Praesent odio ipsum, tincidunt sed tempus in, accumsan eu nunc. Donec quis quam at erat ultricies venenatis. Vivamus ac massa sed massa ultrices faucibus eu a nunc. Nulla mattis eros elementum libero scelerisque non condimentum lorem elementum.</p>
  <a class="abs more" style="left:563px;top:758px">
    <svg width="13" height="10" viewBox="0 0 13 10"><path d="M1 1l4 4-4 4M7 1l4 4-4 4" fill="none" stroke="#1f4f8a" stroke-width="1.8"/></svg>Read More</a>

  <div class="abs feature" style="top:485px">
    <div class="feature-head"><span class="feature-icon"><svg width="10" height="10" viewBox="0 0 10 10"><path d="M3 1l4 4-4 4" fill="none" stroke="#fff" stroke-width="2"/></svg></span><h3>Colleges and Universities</h3></div>
    <p>Aliquam posuere, ante a condimentum adipiscing, mauris tellus vehicula nunc, ac aliquam eros purus id nunc.</p>
  </div>
  <div class="abs feature" style="top:585px">
    <div class="feature-head"><span class="feature-icon"><svg width="10" height="10" viewBox="0 0 10 10"><path d="M3 1l4 4-4 4" fill="none" stroke="#fff" stroke-width="2"/></svg></span><h3>Restaurants</h3></div>
    <p>Aliquam posuere, ante a condimentum adipiscing, mauris tellus vehicula nunc, ac aliquam eros purus id nunc.</p>
  </div>
  <div class="abs feature" style="top:685px">
    <div class="feature-head"><span class="feature-icon"><svg width="10" height="10" viewBox="0 0 10 10"><path d="M3 1l4 4-4 4" fill="none" stroke="#fff" stroke-width="2"/></svg></span><h3>Fitness clubs</h3></div>
    <p>Aliquam posuere, ante a condimentum adipiscing, mauris tellus vehicula nunc, ac aliquam eros purus id nunc.</p>
  </div>
</section>

<section>
  <h2 class="abs sec-title" style="left:80px">PUBS EVENTS</h2>
  <h2 class="abs sec-title" style="left:580px">TESTIMONIALS</h2>
  <div class="abs rule" style="top:883px"></div>

  <div class="abs thumb thumb-party" role="img" aria-label="DJ at a turntable in a nightclub with coloured lights"></div>
  <div class="abs item" style="left:257px;top:911px;width:266px">
    <h4>Morbi lacus velit, adipiscing non</h4>
    <p>Lorem ipsum dolor sit amet, consectetur adipiscing elit. Maecenas euismod fermentum justo, pellentesque magna interdum</p>
  </div>
  <a class="abs more" style="left:443px;top:1039px">
    <svg width="13" height="10" viewBox="0 0 13 10"><path d="M1 1l4 4-4 4M7 1l4 4-4 4" fill="none" stroke="#1f4f8a" stroke-width="1.8"/></svg>Read More</a>

  <div class="abs thumb thumb-person" role="img" aria-label="Portrait of a smiling client"></div>
  <div class="abs item" style="left:768px;top:910px;width:246px">
    <h4>Aenean commodo nisi</h4>
    <p>Lorem ipsum dolor sit amet, consectetur adipiscing elit. Maecenas euismod fermentum justo, pellentesque magna interdum</p>
  </div>
  <a class="abs more" style="left:896px;top:1039px">
    <svg width="13" height="10" viewBox="0 0 13 10"><path d="M1 1l4 4-4 4M7 1l4 4-4 4" fill="none" stroke="#1f4f8a" stroke-width="1.8"/></svg>More Testimonials</a>
</section>

<footer>
  <div class="abs rule" style="top:1087px"></div>
  <p class="abs copyright">Copyright@ 2012.All rights reserved.</p>
  <div class="abs social">
    <span role="img" aria-label="visagebook"></span>
    <span role="img" aria-label="chirpnet"></span>
    <span role="img" aria-label="News feed"></span>
  </div>
  <div class="abs rule" style="top:1143px"></div>
  <div class="abs band"></div>
</footer>

</body>
</html>
```